Skiing Event needs a promotional flyer designed

4 Page A4 brochure to be designed to promote a schools ski event hosted in New Zealand. The brochure will entice School teachers and school students to enter the event. The brochure will provide a basic overview of the event - dates, venue, race options and promote some of the key features of the host mountain.
Event logo has been included. Design overview with copy has been included as word document. Images have been attached that can be used or alternatives sourced. A PDF document has been included of a design example that we like.

Target Market(s)

School Teachers and School Students

Industry/Entity Type

Tourism

Requirements
Must have
• 4 page, A4 portrait document. Must include logo

```html
<!DOCTYPE html>
<html lang="en">
<head>
<meta charset="utf-8">
<title>Mt Kerrow Ski Challenge – Brochure</title>
<link href="https://fonts.googleapis.com/css2?family=Russo+One&family=Lato:wght@400;700&family=Oswald:wght@500&display=swap" rel="stylesheet">
<style>
:root{
  --blue:#1a5eae;
  --blue-deep:#124a92;
  --sky:#3f7fcf;
  --red:#c8193a;
  --ink:#2a2a2a;
  --page-bg:#e6e8eb;
}
*{box-sizing:border-box;margin:0;padding:0}
html,body{width:1200px;height:1200px;overflow:hidden;background:var(--page-bg);font-family:'Lato',sans-serif}
.canvas{position:relative;width:1200px;height:1200px}
.sheet{position:absolute;overflow:hidden;background:#fff;box-shadow:0 4px 14px rgba(0,0,0,.25)}
.sheet--front{left:68px;top:189px;width:525px;height:372px}
.sheet--back{left:630px;top:191px;width:525px;height:375px}
.sheet--inside{left:338px;top:625px;width:531px;height:377px}
.photo{position:absolute}
.wave{position:absolute;left:0;bottom:0;width:100%}

/* front */
.front-photo{inset:0;background:
  radial-gradient(ellipse 120px 150px at 30% 30%,rgba(40,45,60,.55),rgba(40,45,60,0) 70%),
  radial-gradient(ellipse 210px 150px at 75% 28%,rgba(70,95,140,.55),rgba(70,95,140,0) 70%),
  radial-gradient(ellipse 160px 90px at 85% 55%,rgba(255,255,255,.9),rgba(255,255,255,0) 70%),
  linear-gradient(180deg,#2f6fc4 0%,#6e9fdc 25%,#c4d6ec 50%,#eef3f9 70%,#ffffff 100%)}
.title-block{position:absolute;left:76px;top:172px;transform:rotate(-12deg);transform-origin:left top}
.title-box{background:var(--blue);border:3px solid #c9d3de;padding:6px 16px 4px;box-shadow:0 6px 10px rgba(0,0,0,.25);white-space:nowrap}
.title-line{font-family:'Russo One',sans-serif;color:#fff;line-height:1;display:block}
.title-line--small{font-size:29px;padding-left:4px}
.title-line--big{font-size:49px;letter-spacing:1px}
.date-tag{position:absolute;left:248px;top:78px;background:var(--red);color:#fff;padding:6px 12px 5px;font-family:'Russo One',sans-serif;box-shadow:0 4px 8px rgba(0,0,0,.25);white-space:nowrap}
.date-tag__date{font-size:21px;display:block;line-height:1.05}
.date-tag__venue{font-size:11.5px;display:block;letter-spacing:.5px}
.event-mark{position:absolute;right:20px;top:40px;display:flex;align-items:center;gap:5px;font-weight:700;color:#fff;font-size:12px;line-height:1.1;width:104px}
.event-mark__dot{width:14px;height:14px;border-radius:50%;background:#fff;flex:none}
.notice{position:absolute;left:16px;top:266px;display:flex;align-items:center;gap:8px;color:var(--blue);font-size:9.5px;font-weight:700;line-height:1.15}

/* back */
.back-photo{inset:0;background:
  radial-gradient(ellipse 200px 120px at 22% 25%,rgba(170,200,120,.55),rgba(170,200,120,0) 70%),
  radial-gradient(ellipse 160px 60px at 35% 8%,rgba(200,60,80,.45),rgba(200,60,80,0) 70%),
  radial-gradient(ellipse 110px 90px at 75% 45%,rgba(30,50,90,.6),rgba(30,50,90,0) 70%),
  radial-gradient(ellipse 80px 40px at 73% 55%,rgba(40,170,180,.5),rgba(40,170,180,0) 70%),
  linear-gradient(160deg,#7fa1d2 0%,#c6d3e6 35%,#ecdff0 55%,#f4f6fa 80%,#ffffff 100%)}
.contacts{position:absolute;left:0;right:0;bottom:22px;display:flex;justify-content:space-around;color:#fff;font-size:10.5px;font-weight:700;text-align:center}
.contact{display:flex;flex-direction:column;align-items:center;gap:7px}

/* inside */
.inside-photo-top{left:16px;top:11px;width:500px;height:174px;background:
  radial-gradient(ellipse 110px 120px at 28% 60%,rgba(25,25,30,.85),rgba(25,25,30,0) 70%),
  radial-gradient(ellipse 60px 30px at 45% 95%,rgba(40,170,200,.6),rgba(40,170,200,0) 70%),
  radial-gradient(ellipse 200px 80px at 72% 55%,rgba(255,255,255,.8),rgba(255,255,255,0) 70%),
  linear-gradient(180deg,#27324a 0%,#4b5b78 30%,#9fadc0 55%,#e8edf3 85%,#f6f8fb 100%)}
.inside-photo-bottom{left:140px;top:250px;width:391px;height:110px;background:
  radial-gradient(ellipse 110px 70px at 50% 60%,rgba(120,130,145,.7),rgba(120,130,145,0) 70%),
  linear-gradient(180deg,rgba(255,255,255,0) 0%,#e4e8ee 45%,#c3cbd6 100%)}
.col{position:absolute;top:199px;font-size:5.4px;line-height:7.3px;color:var(--ink);text-align:justify}
.col h2{font-size:7.5px;color:var(--red);text-align:center;font-weight:700;margin-bottom:3px}
.col--intro{left:28px;width:103px}
.col--where{left:152px;width:84px}
.col--when{left:250px;width:112px}
.col--who{left:374px;width:140px}
.when-list{list-style:none;font-family:'Oswald',sans-serif;font-size:9.5px;line-height:14px;color:#111;text-align:left;white-space:nowrap}
.when-list li::before{content:"• ";color:var(--red)}
</style>
</head>
<body>
<main class="canvas">

  <section class="sheet sheet--front">
    <div class="photo front-photo" role="img" aria-label="Skier carving through powder snow in front of a snowy mountain peak"></div>
    <div class="event-mark"><span class="event-mark__dot"></span><span>Mt Kerrow Ski Challenge</span></div>
    <div class="title-block">
      <div class="title-box">
        <span class="title-line title-line--small">MT KERROW SKI</span>
        <span class="title-line title-line--big">CHALLENGE</span>
      </div>
      <div class="date-tag">
        <span class="date-tag__date">11-12 JULY 2018</span>
        <span class="date-tag__venue">MT KERROW, NEW ZEALAND</span>
      </div>
    </div>
    <div class="notice">
      <svg width="38" height="38" viewBox="0 0 38 38"><circle cx="19" cy="19" r="16" fill="#fff" stroke="#c8193a" stroke-width="3"/><line x1="8" y1="8" x2="30" y2="30" stroke="#c8193a" stroke-width="3"/></svg>
      <span>NO RACE EXPERIENCE<br>NECESSARY</span>
    </div>
    <svg class="wave" viewBox="0 0 525 70" height="70" preserveAspectRatio="none"><path d="M0 30 C40 18 70 26 100 22 C140 16 170 28 210 24 C250 20 280 10 320 18 C360 26 380 30 420 22 C460 14 490 20 525 30 L525 70 L0 70Z" fill="#1a5eae"/></svg>
  </section>

  <section class="sheet sheet--back">
    <div class="photo back-photo" role="img" aria-label="Skier jumping mid-air over fresh snow, with close-up of ski tips in the background"></div>
    <svg class="wave" viewBox="0 0 525 100" height="100" preserveAspectRatio="none"><path d="M0 28 C30 22 60 10 95 18 C130 26 150 6 185 12 C210 16 220 26 250 20 C280 14 300 2 330 14 C360 24 385 26 410 20 C440 14 470 8 500 14 L525 18 L525 100 L0 100Z" fill="#1a5eae"/></svg>
    <div class="contacts">
      <div class="contact">
        <svg width="18" height="18" viewBox="0 0 18 18"><circle cx="9" cy="9" r="8" fill="none" stroke="#fff" stroke-width="1.3"/><path d="M6 5.5 L7.5 5 L8.3 7 L7.4 7.8 C7.8 8.8 8.8 9.9 9.9 10.4 L10.7 9.5 L12.6 10.3 L12.2 11.9 C9.2 12.4 5.4 8.6 6 5.5Z" fill="#fff"/></svg>
        <span>02 5550 1842</span>
      </div>
      <div class="contact">
        <svg width="18" height="18" viewBox="0 0 18 18"><circle cx="9" cy="9" r="8" fill="none" stroke="#fff" stroke-width="1.3"/><circle cx="9" cy="9" r="4" fill="none" stroke="#fff"/><line x1="5" y1="9" x2="13" y2="9" stroke="#fff"/><ellipse cx="9" cy="9" rx="1.8" ry="4" fill="none" stroke="#fff"/></svg>
        <span>www.kerrowskichallenge.com.au</span>
      </div>
      <div class="contact">
        <svg width="18" height="18" viewBox="0 0 18 18"><circle cx="9" cy="9" r="8" fill="none" stroke="#fff" stroke-width="1.3"/><rect x="5" y="6.5" width="8" height="5.5" fill="none" stroke="#fff"/><path d="M5 6.5 L9 9.5 L13 6.5" fill="none" stroke="#fff"/></svg>
        <span>enquiry@kerrowskichallenge.com.au</span>
      </div>
    </div>
  </section>

  <section class="sheet sheet--inside">
    <div class="photo inside-photo-top" role="img" aria-label="Helmeted skier resting on the snow, looking across a valley of forested ski slopes"></div>
    <div class="photo inside-photo-bottom" role="img" aria-label="Snow-capped mountain peak rising above the clouds"></div>

    <article class="col col--intro">
      <h2>INTRODUCTION</h2>
      <p>We are thrilled to announce the 2018 Mt Kerrow Ski Challenge. The event brings together students from Australia and New Zealand to race on the slopes of Mt Kerrow. It suits novice skiers through to keen racers and snowboarders. No race experience is needed to compete, just a will to give it a go.</p>
      <p>The package offers five great days in the largest ski area in the South Island. Along with two race days, entrants get two days of coaching and a free ski day after the event.</p>
    </article>

    <article class="col col--where">
      <h2>WHERE</h2>
      <p>Held on Mt Kerrow in the Canterbury region of the South Island of New Zealand. The mountain rises to 2086 metres at its top point and gets an average of 4 metres of snow a year.</p>
    </article>

    <article class="col col--when">
      <h2>WHEN</h2>
      <ul class="when-list">
        <li>WEDNESDAY 11TH JULY</li>
        <li>THURSDAY 12TH JULY 2018</li>
      </ul>
    </article>

    <article class="col col--who">
      <h2>WHO</h2>
      <p>The event is open to high school students from across Australia. It welcomes novice and holiday skiers as well as experienced skiers and snowboarders. Prizes are given in each year group for both male and female skiers, plus overall school prizes.</p>
    </article>

    <svg class="wave" viewBox="0 0 531 70" height="70" preserveAspectRatio="none"><path d="M0 38 C40 34 80 28 120 32 C160 36 200 40 240 28 C270 20 300 14 330 22 C360 32 390 40 420 34 C450 28 490 22 531 28 L531 70 L0 70Z" fill="#124a92"/></svg>
  </section>

</main>
</body>
</html>
```